Building Company Business Card Design

I am looking to get a business card designed for my Building Company. Please find the logo attached.

Industry/Entity Type

Business

Contact Information for Business Card

Mobile 0472 913 046
Email admin@tarrowconstructworks.com.au
Website www.tarrowconstructworks.com.au

Colors
0255a3

```html
<!DOCTYPE html>
<html lang="en">
<head>
<meta charset="utf-8">
<title>Tarrow Construct Works – Business Card</title>
<link href="https://fonts.googleapis.com/css2?family=Lato:wght@400;700&display=swap" rel="stylesheet">
<style>
  :root {
    --backdrop: #1e1c1d;
    --brand-blue: #2a55a3;
    --blue-deep: #2650a0;
    --blue-light: #3a88c8;
    --ink-grey: #555a60;
    --rule-grey: #8a8a8a;
    --band-grey: #bdbbbb;
    --band-grey-dark: #9a9a9a;
    --paper: #ffffff;
    --paper-shade: #eef0f2;
  }
  * { margin: 0; padding: 0; box-sizing: border-box; }
  html, body { width: 1200px; height: 1200px; overflow: hidden; }
  body { background: var(--backdrop); font-family: "Lato", sans-serif; position: relative; }

  .card { position: absolute; left: 136px; width: 923px; overflow: hidden; }
  .card--front { top: 20px; height: 565px;
    background: radial-gradient(ellipse at 55% 40%, var(--paper) 30%, var(--paper-shade) 100%);
    border-top: 6px solid var(--brand-blue); }
  .card--back { top: 603px; height: 564px; background: var(--paper); }

  .watermark-map { position: absolute; left: 354px; top: 112px; width: 290px; height: 250px;
    background: rgba(0,0,0,0.03); border-radius: 20px 40px 10px 60px; }
  .watermark-name { position: absolute; left: 0; width: 923px; text-align: center; top: 190px;
    font-size: 60px; font-weight: 700; color: rgba(0,0,0,0.03); white-space: nowrap; }

  .brand-name { position: absolute; font-weight: 700; color: var(--brand-blue);
    white-space: nowrap; letter-spacing: 1px; }
  .card--front .brand-name { left: 0; width: 936px; text-align: center; top: 186px; font-size: 30px; }

  .holder-name { position: absolute; left: 73px; top: 328px; font-size: 37px;
    font-weight: 400; color: var(--ink-grey); }
  .holder-name strong { color: var(--brand-blue); font-weight: 700; }
  .name-rule { position: absolute; left: 89px; top: 372px; width: 744px; height: 2px; background: var(--rule-grey); }

  .contact { position: absolute; left: 461px; top: 386px; font-size: 20px; line-height: 30px; color: var(--ink-grey); }
  .contact .address { margin-bottom: 2px; }
  .contact .link { color: var(--blue-deep); line-height: 29px; }

  .chevrons { position: absolute; left: 0; bottom: 0; }

  .sky-panel { position: absolute; left: 0; top: 0; width: 923px; height: 387px;
    background: radial-gradient(ellipse at 50% 35%, var(--blue-light) 0%, #2e6fba 45%, var(--blue-deep) 100%); }
  .skyline-area { position: absolute; left: 210px; top: 312px; width: 510px; height: 75px;
    background: linear-gradient(to top, rgba(255,255,255,0.75), rgba(255,255,255,0)); }
  .back-name { position: absolute; left: 0; width: 923px; text-align: center; top: 205px;
    font-size: 37px; font-weight: 400; color: var(--paper); }
  .back-name strong { font-weight: 700; }
  .card--back .brand-name { right: 62px; top: 488px; font-size: 30px; }
</style>
</head>
<body>

<section class="card card--front">
  <div class="watermark-map" role="img" aria-label="Faint outline map of New South Wales"></div>
  <div class="watermark-name" aria-hidden="true">TARROW CONSTRUCT WORKS</div>
  <div class="brand-name">TARROW CONSTRUCT WORKS</div>

  <h1 class="holder-name"><strong>YOUR</strong> NAME</h1>
  <div class="name-rule"></div>

  <div class="contact">
    <div class="address">Your address here<br>Harlow Bay Rd, Sydney, NSW, Australia</div>
    <div class="link">0472 913 046</div>
    <div class="link">admin@tarrowconstructworks.com.au</div>
    <div class="link">www.tarrowconstructworks.com.au</div>
  </div>

  <svg class="chevrons" width="923" height="130" viewBox="0 0 923 130">
    <polygon points="0,112 176,2 176,58 74,130 0,130" fill="var(--band-grey)"/>
    <polygon points="182,2 359,116 923,116 923,130 287,130 182,62" fill="var(--blue-deep)"/>
  </svg>
</section>

<section class="card card--back">
  <div class="sky-panel">
    <div class="skyline-area" role="img" aria-label="White silhouette of the Sydney city skyline"></div>
    <h2 class="back-name"><strong>YOUR</strong> NAME</h2>
  </div>
  <div class="brand-name">TARROW CONSTRUCT WORKS</div>
  <svg class="chevrons" width="923" height="120" viewBox="0 0 923 120">
    <polygon points="0,112 176,0 176,56 76,120 0,120" fill="var(--band-grey-dark)"/>
    <polygon points="182,0 359,114 923,114 923,120 282,120 182,58" fill="var(--blue-deep)"/>
  </svg>
</section>

</body>
</html>
```